Building company with a modern and unique product looking for a business card to help us stand out

We currently have a logo but as our business has grown, we feel that our business card is not reflecting our modern and high quality product and help us stand out from the crowd. Our business is mainly in the construction of new homes using a unique method and materials that makes our homes fire proof, vermin and pest resistant and rated to the maximum cyclone category (category 5). We need a business card that helps us stand out as well as communicating professionalism, high quality and trustworthiness. I have attached our current logo with a black and white option, as well as our business card which is double sided. We would like to retain as much of the information that is currently on our business cards, but presented in a more sleek way. We do like our current colour palette ( white, black, yellow and grey) and have been looking primarily at business cards with a black background however we are open to other combinations of colour and layout as long as we stand out. Please feel free to tweak our logo to make it more suitable for a business card, we like the black option that we use but we have had trouble trying to get the white area to match the rest of the logo and blend effectively into a business card. Please do not hesitate to contact us with any questions as we really want this to be successful!

Target Market(s)

Large contracts including government and larger companies

Industry/Entity Type

Business

We will be providing this business card to potential clients including key government ministers and large funding companies, our business card should show that we are professional and reliable.

Requirements
Must have
• It must be easy to read and pleasing to the eye, It must contain as much of the information on the current business card and unless something really stands out, we will most likely pick a design that has all of the information included. It must include our logo of course and have some colour included.
Nice to have
• We are looking for a high end business card and would like to see designs that reflect this. We like the gloss/matte contrast, plastic cards with opaque/coloured areas and unique features not seen on everyday paper business cards. It would be nice to see a few different colour combinations, we are open to new ideas so please feel free to take some artistic licence.
Should not have
• Must not be too busy, difficult to read or be distracting from the information conveyed. Other than this please feel free to add your own touches and make it unique!

```html
<!DOCTYPE html>
<html lang="en">
<head>
<meta charset="utf-8">
<title>Ridgeline Homes Company – Business Card</title>
<link rel="stylesheet" href="https://fonts.googleapis.com/css2?family=Libre+Baskerville&family=Open+Sans:wght@400;600&display=swap">
<style>
  :root {
    --backdrop: #e6e1d8;
    --card-white: #ffffff;
    --card-black: #0b0b0b;
    --brand-gold: #c39d28;
    --text-white: #ffffff;
    --text-black: #111111;
    --rule: rgba(255,255,255,0.55);
  }
  * { margin: 0; padding: 0; box-sizing: border-box; }
  html, body { width: 1200px; height: 900px; overflow: hidden; }
  body {
    background: var(--backdrop);
    position: relative;
    font-family: "Open Sans", Arial, sans-serif;
  }
  .card {
    position: absolute;
    width: 560px;
    height: 320px;
    overflow: hidden;
    box-shadow: 0 10px 28px rgba(0,0,0,0.18);
  }
  /* Front side */
  .card-front {
    left: 360px; top: 110px;
    background: var(--card-white);
    display: flex; align-items: center; justify-content: center;
  }
  .brand {
    display: flex; align-items: center; gap: 14px;
    font-family: "Libre Baskerville", Georgia, serif;
    font-weight: 400;
  }
  .brand-mark {
    width: 18px; height: 18px;
    background: var(--brand-gold);
  }
  .card-front .brand-name {
    font-size: 34px; color: var(--text-black); line-height: 1.1;
  }
  .brand-sub {
    display: block; font-size: 17px; margin-top: 4px;
  }
  /* Back side */
  .card-back {
    left: 300px; top: 480px;
    background: var(--card-black);
  }
  .gold-field {
    position: absolute; inset: 0;
    background: var(--brand-gold);
    clip-path: polygon(0 36%, 100% 74%, 100% 100%, 0 100%);
  }
  .card-back .brand {
    position: absolute; right: 34px; top: 34px;
  }
  .card-back .brand-name {
    font-size: 26px; color: var(--text-white); text-align: right; line-height: 1.1;
  }
  .card-back .brand-sub { font-size: 14px; }
  .person {
    position: absolute; left: 30px; top: 150px;
    color: var(--text-white);
  }
  .person-name {
    font-family: "Libre Baskerville", Georgia, serif;
    font-size: 22px; letter-spacing: 0.5px;
  }
  .person-title {
    font-family: "Libre Baskerville", Georgia, serif;
    font-size: 13px; margin-top: 4px;
  }
  .contacts {
    position: absolute; left: 30px; right: 24px; bottom: 26px;
    display: flex; align-items: center; gap: 20px;
    color: var(--text-white); font-size: 13px;
  }
  .contact-group {
    display: flex; flex-direction: column; gap: 6px;
    padding-left: 20px; border-left: 1px solid var(--rule);
  }
  .contact-line { display: flex; align-items: center; gap: 8px; }
  .contact-icon { width: 13px; height: 13px; flex: none; }
</style>
</head>
<body>

  <section class="card card-front" aria-label="Business card front">
    <div class="brand">
      <span class="brand-mark"></span>
      <span class="brand-name">Ridgeline Homes<span class="brand-sub">Company</span></span>
    </div>
  </section>

  <section class="card card-back" aria-label="Business card back">
    <div class="gold-field"></div>

    <div class="brand">
      <span class="brand-name">Ridgeline Homes<span class="brand-sub">Company</span></span>
    </div>

    <div class="person">
      <p class="person-name">Daniel Moreau</p>
      <p class="person-title">Managing Director</p>
    </div>

    <div class="contacts">
      <div class="contact-group">
        <p class="contact-line">
          <svg class="contact-icon" viewBox="0 0 16 16" aria-hidden="true"><path fill="#fff" d="M3.5 1l2.5 3-1.5 2c1 2 3 4 5 5l2-1.5 3 2.5-1.5 2.5C8 15 1 8 1 2.5z"/></svg>
          0400 555 123
        </p>
        <p class="contact-line">
          <svg class="contact-icon" viewBox="0 0 16 16" aria-hidden="true"><rect x="4" y="1" width="8" height="14" rx="1.5" fill="none" stroke="#fff" stroke-width="1.6"/><circle cx="8" cy="12.5" r="0.9" fill="#fff"/></svg>
          (02) 5550 1234
        </p>
      </div>
      <div class="contact-group">
        <p class="contact-line">
          <svg class="contact-icon" viewBox="0 0 16 16" aria-hidden="true"><rect x="1" y="3" width="14" height="10" rx="1" fill="#fff"/><path d="M1.5 3.5L8 9l6.5-5.5" fill="none" stroke="#c39d28" stroke-width="1.4"/></svg>
          hello@ridgelinehomes.com
        </p>
        <p class="contact-line">
          <svg class="contact-icon" viewBox="0 0 16 16" aria-hidden="true"><circle cx="8" cy="8" r="6.5" fill="none" stroke="#fff" stroke-width="1.5"/><path d="M1.5 8h13M8 1.5c-2.5 3-2.5 10 0 13M8 1.5c2.5 3 2.5 10 0 13" fill="none" stroke="#fff" stroke-width="1.1"/></svg>
          www.ridgelinehomes.com
        </p>
      </div>
    </div>
  </section>

</body>
</html>
```